Website for 9 year old artist, helps animal rescue charity :)

I am looking to have a simple website created for my 9 year old son's small "company." He makes necklaces and art out of beachcombed treasures and sells them for animal rescue charity. Currently, his domain name www.gullcovepebblecraft.com brings people straight to his friendvine page, but for those who are not on FV, nothing shows up.

I would like a simple landing page + a few other clickable pages that will show his logo (already done by Pixel Assembly folks!) +
* photos
* a brief description about what he does
* a link to the charities he supports
* link to his Friendvine Page (https://www.friendvine.com/GullCovePebblecraft)
* are where a link to a possible craftly store could go (future, we haven't gotten that far). :)
(really just a "shop" button)
I need to be able to add and remove photos and text, add calendar dates of events he will be at, and adjust links if needed.

I hope this isn't too complicated! It doesn't need to be flashy, just an easy on the eyes page where people who are interested in his necklaces and his charity work can go to find out more. I would like to have the website incorporate the two logos (see uploads). I image the image of the child beachcombing being on the bottom anchoring the page, but that is as far as my imagination has gone regarding the web design! :)

UPDATED:
Name of web url: www.gullcovepebblecraft.com
Name of company: Gull Cove Pebblecraft
Purpose: Milo is 9 years old. He beachcombs with his family all over the United States and finds wonderful shells, seaglass, and pottery. His mom helps him drill the holes in these piece and then he creates one of a kind necklaces using these beachcombed treasures and silver charms. He also makes sweet shell, seaglass and driftwood angels (Milo's Cherubs). All shells are responsibly collected. Every piece is designed by Milo.

At least 20% off all proceeds from every sale goes to animal rescue charity.

Target Market(s)

The target market for his necklaces is typically women, but we have a lot of guys buy them, too, to hang in their windows or to give away. All ages of folks buy his necklaces at the small sales and fairs we have gone to. They also look at his site to find out more about Willow Paws Cat Rescue, the organization Milo donates a lot of his proceeds to.

We get a lot of requests about whether he has a webpage and find that many of the people who want to check it out do not have Friendvine, so linking right to FV hasn't worked.

Industry/Entity Type

Charity

Requirements
Must have
• * Logos (I have 2 done by design works folks). The one of the beachcombing child is for the website only, the one of the shell angel will be for the website and business cards, etc.
* Spaces for photos
* Clickable links to Friendvine, Craftly (later), charity(s) he donates to
* Space for Bio/backstory
* Contact us area

Match the blues of the two logos so they are the same shade.

The look should be young and simple, without being childish. We are beachcombers at heart, so sea and sand colors would work great. All blues (except electric), greens, tans, etc are great.

I added a ton of images for reference. Please message me if you would like more.
Nice to have
• * Area I can add the tally of how much he has donated so far
* Slideshow of images (I uploaded a ton for examples)
* Page dedicated to images and information about the of the rescue organization he primarily donates to. The rescue organization is dedicated to the rehabilitation and adoption of special needs and abused cats.
Should not have
• Curlz font or anything too cutesy

Bright colors, I am hoping for a more muted, seas-inspired look.

```html
<!DOCTYPE html>
<html lang="en">
<head>
<meta charset="utf-8">
<title>Gull Cove Pebblecraft</title>
<link rel="stylesheet" href="https://fonts.googleapis.com/css2?family=Open+Sans:wght@300;400;600&family=PT+Sans:wght@400;700&display=swap">
<style>
:root{
  --sand:#f2eee7;
  --sand-dark:#e4ddd0;
  --tan-top:#cbb993;
  --tan-bottom:#8e7a56;
  --tan-line:#a6946f;
  --sea:#1fc3dd;
  --sea-deep:#08a0c6;
  --sea-button:#0b86aa;
  --foam:#d5eef6;
  --ink:#4a4a4a;
  --heading:#2f2f2f;
  --social:#8a8379;
  --white:#ffffff;
}
*{margin:0;padding:0;box-sizing:border-box}
html,body{width:1043px;height:1200px;overflow:hidden;background:var(--white)}
body{font-family:"Open Sans",sans-serif;color:var(--ink);position:relative}

.hero{position:absolute;left:0;top:0;width:1043px;height:584px;
  background:linear-gradient(180deg,#a7adb2 0%,#6f7881 16%,#3c4552 40%,#2b2f38 70%,#3a3a3e 100%)}
.hero-photo{position:absolute;inset:0;
  background:radial-gradient(ellipse at 30% 55%,rgba(40,60,110,.55),transparent 55%),
             radial-gradient(ellipse at 78% 72%,rgba(170,160,145,.45),transparent 40%)}
.hero-caption{position:absolute;left:0;right:0;top:294px;text-align:center;color:var(--white);
  font-family:"PT Sans",sans-serif;text-shadow:0 1px 3px rgba(0,0,0,.4)}
.hero-caption h1{font-weight:400;font-size:43px;line-height:52px}
.hero-caption p{font-weight:400;font-size:22px;line-height:28px}
.hero-arrow{position:absolute;top:294px}
.hero-arrow.prev{left:66px}
.hero-arrow.next{left:944px}

.main-nav{position:absolute;left:67px;top:87px;width:909px;height:50px;
  background:linear-gradient(180deg,var(--tan-top),var(--tan-bottom));border-radius:3px;
  box-shadow:0 1px 2px rgba(0,0,0,.35)}
.main-nav a{position:absolute;top:0;height:50px;line-height:50px;color:var(--white);
  font-family:"PT Sans",sans-serif;text-decoration:none;font-size:18px;text-shadow:0 1px 1px rgba(0,0,0,.25)}
.main-nav .sep{position:absolute;top:0;width:1px;height:50px;background:var(--tan-line)}

.brand{position:absolute;left:424px;top:8px;width:196px;height:196px;border-radius:50%;
  background:rgba(255,255,255,.55);display:flex;align-items:center;justify-content:center}
.brand-inner{width:172px;height:172px;border-radius:50%;background:var(--white);
  display:flex;flex-direction:column;align-items:center;justify-content:center;gap:8px}
.brand-dot{width:62px;height:62px;border-radius:50%;background:var(--sea)}
.brand-name{color:var(--sea);font-family:"PT Sans",sans-serif;font-size:16px;font-weight:400;text-align:center;line-height:18px;width:120px}

.feature{position:absolute;top:600px;width:290px;height:134px}
.feature-box{position:absolute;left:0;top:0;width:290px;height:130px;border-radius:3px 3px 0 0;
  background:linear-gradient(180deg,var(--sea) 0%,var(--sea-deep) 100%)}
.feature-base{position:absolute;left:0;top:128px;width:290px;height:7px;background:var(--sand-dark);border-bottom:1px solid #b9ab90}
.feature h2{position:absolute;left:22px;top:18px;font-family:"PT Sans",sans-serif;font-weight:400;font-size:24px;line-height:30px;color:var(--white);white-space:nowrap}
.feature p{position:absolute;left:23px;top:55px;width:160px;font-size:10.5px;line-height:16px;color:var(--white);font-weight:300}
.feature .btn{position:absolute;left:22px;top:92px;height:24px;padding:0 15px;line-height:24px;
  background:var(--sea-button);color:var(--white);font-family:"PT Sans",sans-serif;font-size:12px;text-decoration:none;border-radius:2px}
.feature .icon{position:absolute}

.divider{position:absolute;left:67px;top:784px;width:913px;border-top:1px dotted #bdbdbd}

.walker{position:absolute;left:27px;top:834px;width:133px;height:337px;
  background:linear-gradient(180deg,#aee0ef,#8fd3ea);opacity:.75;border-radius:60px 60px 20px 20px}

.about{position:absolute;left:71px;top:818px;width:557px}
.about h2{font-weight:300;font-size:28px;color:var(--heading);margin-bottom:10px}
.about p{font-size:11.5px;line-height:19.5px;font-weight:300;color:var(--ink);margin-bottom:12px;position:relative}

.photos{position:absolute;left:667px;top:818px}
.photos h2{font-weight:300;font-size:25px;color:var(--heading)}
.thumb{position:absolute;width:92px;height:71px;border-radius:2px}

.shore{position:absolute;left:0;top:1091px;width:1043px;height:109px;background:var(--sand)}
.shore .wave{position:absolute;left:0;width:1043px;background:var(--foam)}
.copyright{position:absolute;left:0;right:0;top:1151px;text-align:center;font-size:12px;font-weight:300;color:#5b5b5b}
.social{position:absolute;top:1149px;width:28px;height:28px;border-radius:50%;background:var(--social)}
</style>
</head>
<body>

<section class="hero">
  <div class="hero-photo" role="img" aria-label="Photo of a boy smiling beside stacked beach stones on dark shoreline rocks with waves behind"></div>
  <svg class="hero-arrow prev" width="36" height="72" viewBox="0 0 36 72"><polyline points="34,2 2,36 34,70" fill="none" stroke="rgba(255,255,255,.7)" stroke-width="2"/></svg>
  <svg class="hero-arrow next" width="36" height="72" viewBox="0 0 36 72"><polyline points="2,2 34,36 2,70" fill="none" stroke="rgba(255,255,255,.7)" stroke-width="2"/></svg>
  <div class="hero-caption">
    <h1>Mauris vel lacus vitae felis vestibulum</h1>
    <p>Nulla elementum dui ut augu Aliquam vehicula mi</p>
  </div>
</section>

<nav class="main-nav">
  <a href="#" style="left:59px">Main</a><span class="sep" style="left:116px"></span>
  <a href="#" style="left:139px">About Us</a><span class="sep" style="left:229px"></span>
  <a href="#" style="left:251px">Products</a>
  <a href="#" style="left:582px">Charity</a><span class="sep" style="left:656px"></span>
  <a href="#" style="left:679px">Buy Now</a><span class="sep" style="left:764px"></span>
  <a href="#" style="left:788px">Contact</a>
</nav>

<div class="brand">
  <div class="brand-inner">
    <span class="brand-dot"></span>
    <span class="brand-name">Gull Cove Pebblecraft</span>
  </div>
</div>

<article class="feature" style="left:67px">
  <div class="feature-box"></div><div class="feature-base"></div>
  <h2>Chairty Support</h2>
  <p>Mauris vel lacus vitae felis vesti bulum volutpat.</p>
  <a class="btn" href="#">CLICK HERE</a>
  <svg class="icon" style="left:190px;top:20px" width="82" height="84" viewBox="0 0 82 84">
    <text x="34" y="46" text-anchor="middle" font-family="Open Sans,sans-serif" font-weight="600" font-size="48" fill="#fff">$</text>
    <path d="M2 62 h22 l14 -6 h22 l18 -10 l4 4 l-20 22 l-20 8 h-24 l-16 -8z" fill="#fff"/>
  </svg>
</article>

<article class="feature" style="left:380px">
  <div class="feature-box"></div><div class="feature-base"></div>
  <h2>Friendvine Connect</h2>
  <p style="width:185px">Mauris vel lacus vitae felis vestibulum volutpat. Etiam est nunc venenatis</p>
  <a class="btn" href="#">CLICK HERE</a>
  <svg class="icon" style="left:230px;top:40px" width="50" height="50" viewBox="0 0 50 50" aria-label="Friendvine">
    <rect x="1" y="1" width="48" height="48" rx="9" fill="#fff"/>
  </svg>
</article>

<article class="feature" style="left:691px">
  <div class="feature-box"></div><div class="feature-base"></div>
  <h2>Possibel Store</h2>
  <p style="width:170px">Mauris vel lacus vitae felis vestibu-lum volutpat. Etiam est nunc</p>
  <a class="btn" href="#">CLICK HERE</a>
  <svg class="icon" style="left:196px;top:28px" width="80" height="74" viewBox="0 0 80 74">
    <rect x="10" y="2" width="60" height="8" fill="#fff"/>
    <path d="M4 12 h72 l4 14 c0 6 -10 6 -10 0 c0 6 -12 6 -12 0 c0 6 -12 6 -12 0 c0 6 -12 6 -12 0 c0 6 -12 6 -12 0 c0 6 -10 6 -10 0z" fill="#fff"/>
    <path d="M10 32 v38 h60 v-38 h-6 v24 h-48 v-24z" fill="#fff"/>
  </svg>
</article>

<div class="divider"></div>

<div class="walker" role="img" aria-label="Light blue silhouette of a child walking along the shore"></div>

<section class="about">
  <h2>Little About Me</h2>
  <p>Mauris vel lacus vitae felis vestibulum volutpat. Etiam est nunc, venenatis in, tristique eu, imperdiet ac, nisl. Cum sociis natoque penatibus et magnis dis parturient montes, nascetur ridiculus mus. In iaculis facilisis massa. Etiam eu urna. Sed porta. Suspendisse quam leo, molestie sed, luctus quis, feugiat in, pede. Fusce tellus. Sed metus augue, convallis et, vehicula ut, pulvinar eu, ante. Integer orci tellus, tristique vitae, consequat nec, porta vel, lectus. Nulla sit amet diam. Duis non nunc</p>
  <p>Vivamus porttitor, g, purus nisi eleifend libero, a tempus libero lectus feugiat felis. Morbi diam mauris, viverra in, gravida eu, mattis in, ante. Morbi eget arcu. Morbi porta, libero id ullamcorper nonummy, nibh ligula pulvinar metus, eget consectetuer augue nisi quis lacus.</p>
</section>

<section class="photos">
  <h2>Recent Photos</h2>
</section>
<div class="thumb" style="left:669px;top:857px;background:linear-gradient(135deg,#d8cbb8,#8a6d55)" role="img" aria-label="Pile of collected seashells"></div>
<div class="thumb" style="left:777px;top:857px;background:linear-gradient(135deg,#a9a37c,#5f7a4a)" role="img" aria-label="Sea glass necklaces with starfish charms"></div>
<div class="thumb" style="left:884px;top:857px;background:linear-gradient(135deg,#6b5a48,#9fb4c8)" role="img" aria-label="Shell and sea glass pendants on wood"></div>
<div class="thumb" style="left:669px;top:941px;background:linear-gradient(135deg,#a88e74,#4b3e36)" role="img" aria-label="Heart shaped stone among beach pebbles"></div>
<div class="thumb" style="left:777px;top:941px;background:linear-gradient(135deg,#c7c2b0,#8fb3a6)" role="img" aria-label="Pale sea glass pieces"></div>
<div class="thumb" style="left:884px;top:941px;background:linear-gradient(135deg,#3f7a4a,#b7c7a8)" role="img" aria-label="Green glass float with silver charm"></div>

<footer class="shore">
  <div class="wave" style="top:0;height:6px"></div>
  <div class="wave" style="top:14px;height:10px;opacity:.8"></div>
  <div class="wave" style="top:32px;height:6px;opacity:.6"></div>
</footer>
<p class="copyright">Copyright © 2013 Company Name.&nbsp; All right reserved.</p>
<a class="social" style="left:858px" href="#" aria-label="Friendvine"></a>
<a class="social" style="left:889px" href="#" aria-label="Chirper"></a>
<a class="social" style="left:920px" href="#" aria-label="Linkwork"></a>
<a class="social" style="left:951px" href="#" aria-label="Photoflock"></a>

</body>
</html>
```